Vertical flyer design to guide people to my shop

We need a vertical flyer design for a tailor shop, Marlow Stitchworks. Our shop is on the 3/F, and we need this flyer/poster to placed on the G/F street level to guide people to take the lifts upstairs. Basically to tell people that, "We are here on 3/F!"

Dimensions ratio: 80 (wide) x200 (tall)

You may use the photos and graphics from the webpages below.
http://www.marlowstitchworks.net/en/marlow-stitchworks-hong-kong-tailors-tailor-shop/

https://www.cloth-q.com/tailor/marlow-stitchworks

```html
<!DOCTYPE html>
<html lang="en">
<head>
<meta charset="utf-8">
<title>Marlow Stitchworks – We Are Here on 3/F</title>
<link href="https://fonts.googleapis.com/css2?family=Tinos:wght@400;700&display=swap" rel="stylesheet">
<style>
  :root {
    --ink: #111111;
    --paper: #ffffff;
    --stage: #e4e4e4;
    --panel-dark: #2b2b2b;
    --band-dark: #1c1c1c;
    --band-mid: #2a2a2a;
    --photo-grey-a: #9a9c9e;
    --photo-grey-b: #4a4c50;
    --photo-warm-a: #1a1714;
    --photo-warm-b: #6d645a;
    --photo-cloth-a: #5a5a5a;
    --photo-cloth-b: #cfcfcf;
  }
  * { margin: 0; padding: 0; box-sizing: border-box; }
  html, body { width: 848px; height: 1200px; overflow: hidden; background: var(--stage); }
  .flyer {
    position: absolute; left: 184px; top: 0; width: 480px; height: 1200px; overflow: hidden;
    background: var(--paper); color: var(--ink);
    font-family: "Tinos", "Times New Roman", serif;
  }
  .abs { position: absolute; }

  .hero-photo {
    left: 0; top: 0; width: 480px; height: 300px;
    background: linear-gradient(100deg, var(--photo-grey-b) 0%, #6f7174 35%, var(--photo-grey-a) 65%, #b7b8b9 100%);
  }
  .title-box {
    left: 80px; top: 178px; width: 320px; height: 236px;
    border: 2px solid var(--ink);
  }
  .title-name {
    left: 80px; top: 190px; width: 320px; text-align: center;
    color: var(--paper); font-weight: 700; font-size: 34px; line-height: 48px;
  }
  .title-sub {
    left: 80px; top: 314px; width: 320px; text-align: center;
    font-size: 24px; line-height: 42px;
  }

  .rack-photo {
    left: 0; top: 454px; width: 300px; height: 296px;
    background: linear-gradient(90deg, var(--photo-warm-a) 0%, var(--photo-warm-b) 40%, #3a3530 70%, var(--photo-warm-a) 100%);
  }
  .quality-card {
    left: 176px; top: 484px; width: 284px; height: 228px;
    background: var(--paper);
  }
  .quality-rule { left: 176px; top: 712px; width: 284px; height: 7px; background: var(--ink); }
  .quality-list {
    left: 196px; top: 528px; font-size: 20px; line-height: 44px; list-style: none;
  }

  .fit-panel {
    left: 0; top: 790px; width: 292px; height: 200px; background: var(--panel-dark);
  }
  .fit-list {
    left: 24px; top: 826px; color: var(--paper); font-size: 20px; line-height: 44px; list-style: none;
  }
  .cloth-photo {
    left: 292px; top: 790px; width: 188px; height: 200px;
    background: linear-gradient(120deg, var(--photo-cloth-a) 0%, var(--photo-cloth-b) 45%, #8d8d8d 75%, var(--photo-cloth-a) 100%);
  }
  .dash-lines { left: 0; top: 990px; }

  .floor-band { left: 0; top: 1050px; width: 480px; height: 150px; background: var(--band-dark); }
  .floor-band-end { left: 318px; top: 1050px; width: 162px; height: 150px; background: var(--band-mid); }
  .floor-invite {
    left: 12px; top: 1095px; color: var(--paper); font-size: 20px; line-height: 30px;
  }
  .floor-on {
    left: 224px; top: 1085px; color: var(--paper); font-size: 58px; line-height: 80px;
  }
  .floor-level {
    left: 332px; top: 1085px; height: 80px; color: var(--paper); font-size: 54px; line-height: 80px;
    display: flex; align-items: center; gap: 12px;
  }
</style>
</head>
<body>
<main class="flyer">
  <div class="abs hero-photo" role="img" aria-label="Photo of two men in tailored suits seated on a rooftop ledge"></div>
  <div class="abs title-box"></div>
  <h1 class="abs title-name">MARLOW<br>STITCHWORKS</h1>
  <p class="abs title-sub">EXPERT LADIES’<br>&amp; GENT’S TAILORS</p>

  <div class="abs rack-photo" role="img" aria-label="Photo of tailored jackets hanging on a rail"></div>
  <div class="abs quality-card"></div>
  <div class="abs quality-rule"></div>
  <ul class="abs quality-list">
    <li>FOR LADIES’ &amp; GENTS’</li>
    <li>BEST QUALITY</li>
    <li>EXPERT TAILOR</li>
  </ul>

  <div class="abs fit-panel"></div>
  <ul class="abs fit-list">
    <li>PERFECT FIT</li>
    <li>LUXURY</li>
    <li>MARLOW STITCHWORKS</li>
  </ul>
  <div class="abs cloth-photo" role="img" aria-label="Photo of a shirt placket with a yellow tape measure"></div>

  <svg class="abs dash-lines" width="480" height="60" viewBox="0 0 480 60" aria-hidden="true">
    <line x1="0" y1="4" x2="480" y2="4" stroke="#2b2b2b" stroke-width="3" stroke-dasharray="9 4"/>
    <line x1="0" y1="52" x2="480" y2="52" stroke="#1c1c1c" stroke-width="3" stroke-dasharray="9 4"/>
  </svg>

  <div class="abs floor-band"></div>
  <div class="abs floor-band-end"></div>
  <p class="abs floor-invite">WE ARE HERE &amp;<br>VISIT OUR STORE</p>
  <p class="abs floor-on">ON</p>
  <p class="abs floor-level">
    <svg width="30" height="28" viewBox="0 0 30 28" aria-hidden="true">
      <polyline points="3,3 13,14 3,25" fill="none" stroke="#ffffff" stroke-width="3"/>
      <polyline points="15,3 25,14 15,25" fill="none" stroke="#ffffff" stroke-width="3"/>
    </svg>
    <span>3/F</span>
  </p>
</main>
</body>
</html>
```